Nine Quiet Hours
Business Cards & Letterhead for Sleep Therapist - Health
Business Cards & Letterhead for Sleep Therapist
Professional
Nola J. Barnes, MA, RPSGT, RST, RCC
Founder - Sleep Therapist
4862 Fenwick Avenue, Suite 214 Toronto, ON M6P 2K8
855.52Hushh (855.527.3381)
nola@ninequiethours.example
www.ninequiethours.example www.nineq-hours.example
Front of card should be logo with the tagline "Sleep Consultants and Coaching" on mainly white background, and contact information as provided. I have a few versions of my logo -- I'd like to see both mocked up.
Dark background (black, navy or midnight blue) logo with the tagline "bright ideas for better sleep" & web addresses
jlbarnes jlbarnes
Sincerely, thank you to all the designers who submitted to my project ... I am so pleased with the quality of work.
Hello Designers, I'd appreciate not seeing full stationary design submissions until a business card layout you have submitted has been narrowed to a finalist. There are so many great and unique designs to review ... your time and mine is valuable. So, I will request to see the stationary package options from you when I have selected a business card design of yours that is remaining as one of my finalists. thank you!
Great start! Wow. Thank you for the submissions so far ... general feedback for now, with private feedback to follow soon: 1) please don't merge the two logo concepts (with rare exception - if you have stars on a design now that did this, you've done a unique job that somehow is working for me) The light blue sheep with white and black is one complete look. The yellow moon-bulb with white and midnight blue/navy or black is another complete look. I hope to see/have these two versions of the winning design layout. 2) the light blue as a full colour background for the back of the card doesn't work. I prefer black background with the sheep design on the back of the card. 3) do not use the Hushh for the toll free phone number just the numbers 855.527.3381 and please be sure to denote this as 'toll free' or TF. 4) please make sure both web addresses appear on the card ... if one is used on the front, the other must appear on the back. Or both can appear on the back only ... but both must appear. 5) both logo designs need the tagline "Sleep Coach and Consulting" (no quotation marks though) on the front of the card ... and "bright ideas for better sleep" (all lower case, no quotation marks) on the back of the card. Cheers! I'll do a fresh round of star ratings shortly
I'm open to creative interpretation of my directions ... ie. Logo on the back can be just an element of same (moon-bulb, sheep), larger watermark, etc.? The tagline does not have to reside just under the logo ... Although the front of the cards should be light background & back dark background I don't mind some of the creative touches that tie the sides together more artistically. You're the pros, so I look forward to seeing what is submitted!

```html
<!DOCTYPE html>
<html lang="en">
<head>
<meta charset="utf-8">
<title>Nine Quiet Hours — Business Cards</title>
<link href="https://fonts.googleapis.com/css2?family=Varela+Round&family=Open+Sans:wght@400;600&display=swap" rel="stylesheet">
<style>
  :root {
    --stage: #2a2a2c;
    --card-dark: #2e3033;
    --card-dark-edge: #232427;
    --card-light: #ffffff;
    --teal: #7ec8c9;
    --teal-soft: #c8e9e9;
    --ink: #3a3b3d;
    --ink-soft: #6d6f72;
    --grey-text: #b9bcbf;
  }
  * { box-sizing: border-box; margin: 0; padding: 0; }
  html, body {
    width: 1200px; height: 751px; overflow: hidden;
    background: var(--stage);
    font-family: "Open Sans", sans-serif;
  }
  .sheet {
    position: relative; width: 1200px; height: 751px;
    display: flex; align-items: center; justify-content: center; gap: 28px;
  }
  .card {
    position: relative; width: 558px; height: 319px;
    border-radius: 14px; overflow: hidden;
  }

  /* Back side */
  .card--back {
    background: linear-gradient(160deg, var(--card-dark) 0%, var(--card-dark-edge) 100%);
  }
  .card--back .watermark {
    position: absolute; left: 0; top: 0; width: 290px; height: 319px;
    background: linear-gradient(90deg, rgba(255,255,255,0.05) 0%, rgba(255,255,255,0) 100%);
  }
  .card--back .brand {
    position: absolute; left: 300px; top: 70px; width: 230px; text-align: center;
  }
  .brand-mark {
    display: block; margin: 0 auto 10px;
    width: 58px; height: 58px; border-radius: 50%;
    background: var(--teal);
  }
  .brand-name {
    font-family: "Varela Round", sans-serif;
    font-size: 24px; letter-spacing: 0.5px; white-space: nowrap;
  }
  .card--back .brand-name { color: #ffffff; }
  .card--back .tagline {
    margin-top: 4px; font-size: 11px; color: var(--teal);
    font-family: "Varela Round", sans-serif;
  }
  .card--back .web {
    margin-top: 22px; font-size: 11px; line-height: 1.6; color: var(--grey-text);
  }

  /* Front side */
  .card--front { background: var(--card-light); }
  .card--front .art-area {
    position: absolute; left: 0; top: 0; width: 300px; height: 319px;
    background: linear-gradient(90deg, var(--teal) 0%, var(--teal-soft) 65%, var(--card-light) 100%);
  }
  .card--front .brand {
    position: absolute; left: 40px; top: 112px; width: 210px; text-align: center;
  }
  .card--front .brand-mark { background: var(--ink); width: 48px; height: 48px; }
  .card--front .brand-name { color: var(--ink); font-size: 21px; }
  .card--front .tagline {
    margin-top: 3px; font-size: 10px; color: var(--ink);
    font-family: "Varela Round", sans-serif;
  }
  .contact {
    position: absolute; right: 28px; top: 34px; width: 230px; text-align: right;
    color: var(--ink-soft); font-size: 10.5px; line-height: 1.55;
  }
  .contact .person {
    font-family: "Varela Round", sans-serif;
    font-size: 17px; color: var(--teal); line-height: 1.2;
  }
  .contact .creds { font-size: 10px; }
  .contact .role { font-weight: 600; color: var(--ink); margin-bottom: 14px; }
  .contact .address { margin-bottom: 14px; }
  .contact .email { color: var(--ink); }
</style>
</head>
<body>
<main class="sheet">
  <section class="card card--back" aria-label="Business card back">
    <div class="watermark" role="img" aria-label="Faint large brand symbol watermark"></div>
    <div class="brand">
      <span class="brand-mark"></span>
      <div class="brand-name">Nine Quiet Hours</div>
      <div class="tagline">bright ideas for better sleep</div>
      <div class="web">
        <div>www.ninequiethours.example</div>
        <div>www.nineq-hours.example</div>
      </div>
    </div>
  </section>

  <section class="card card--front" aria-label="Business card front">
    <div class="art-area" role="img" aria-label="Teal moon and light bulb illustration with stars"></div>
    <div class="brand">
      <span class="brand-mark"></span>
      <div class="brand-name">Nine Quiet Hours</div>
      <div class="tagline">Sleep Coach and Consulting</div>
    </div>
    <div class="contact">
      <div class="person">Nola J. Barnes</div>
      <div class="creds">MA, RPSGT, RST, RCC</div>
      <div class="role">Founder - Sleep Therapist</div>
      <div class="address">
        <div>4862 Fenwick Avenue</div>
        <div>Suite 214</div>
        <div>Toronto, ON M6P 2K8</div>
      </div>
      <div>(TF) 855.527.3381</div>
      <div class="email">nola@ninequiethours.example</div>
    </div>
  </section>
</main>
</body>
</html>
```